Starter & Alternator business needs a website

update: very good designs submitted so far. also need this to display well on mobile devices. not sure if wordpress or html/css is better for my needs.

Our existing website is vellumtorq.com and is need of total revamp. Need full design of a website for my business.

We sell and rebuild starters and alternators. Customers bring in the units and we rebuild them. Or we sell them brand new or rebuilt units we have in stock. We do not install units into vehicles like a mechanic would. We strictly rebuild starters and alternators in our shop, sell brand new units over the counter, and we do deliver occasionally as well. We do offer a line of Orvan batteries as well but that is only a small feature of the business.

I would like this website designed and coded. I can upload the files to my web host after completion. I can also add in and modify content like our background info, etc.

I have included an illustrator file that shows some of our signage and logo, etc. I have also included a radio commercial sample so you can get a little better feel for the business. A similar ad does run on the radio currently, slightly different and without the added sound effects.

Update: I do like using photos of real items(starters or alternators etc) for an icon, like a real alternator stock image for the alternator section icon, etc. Maybe incorporate our logo in that design as well. That looks nice as well and may aid in navigation.

For any other design elements, do what you think looks good. Our colors are red/white/blue as seen in the illustrator file. our building is painted with halbeck moray colors, ember gala red and deep tide for blue.

Here are some examples of rebuilders websites in other markets for reference:

https://quillmarauto.com/starter-alternator-rebuilding/

https://www.dunwickmotorworks.com/auto-repairs/alternator-starter-rebuilds.aspx

https://www.fjordvoltage.com/

https://www.pemberlowgx.com/

The website can have areas for: services and products offered, high output alternators, Orvan Batteries, troubleshooting tips, current specials, contact info and directions/map, etc. Whatever else you feel applies.

At some point I do want to be able to sell items directly online or at least have a secure section for customers to submit invoice payments, but that's not necessarily in scope for this project just something to keep in mind.

Target Market(s)

Mechanics and Managers in fleet shops, construction and marine industries, shipping trades. Also automobile owners who work on their own vehicles. We sell and rebuild starters and alternators for automobiles, heavy duty equipment, forklifts, traxlifts, man movers, ferrettes, loaders, large tractors and trucks, just about any engine, golf carts, generators, etc.

Industry/Entity Type

Automotive Part

Coding

Coded - Design and coding required

Number of Pages Required

5+ page

Font styles to use
Serif
Sans Serif

Colors
0255a3
ec1f27
ffffff

Requirements
Must have
• Should also display nicely on mobile phones. Highlight our specialty, "Starters & Alternators"

```html
<!DOCTYPE html>
<html lang="en">
<head>
<meta charset="utf-8">
<title>Kalena Rebuild Co. — Starters &amp; Alternators</title>
<link href="https://fonts.googleapis.com/css2?family=Cabin:wght@500;600;700&family=Source+Sans+3:wght@400;600;700&display=swap" rel="stylesheet">
<style>
:root{
  --red:#be2228;
  --red-dark:#9c1a1f;
  --navy:#213b73;
  --navy-dark:#1a2f5c;
  --ink:#222;
  --muted:#555;
  --line:#d9d9d9;
  --footer:#2b2b2b;
  --white:#fff;
}
*{box-sizing:border-box;margin:0;padding:0}
html,body{width:1200px;height:4528px;overflow:hidden}
body{font-family:"Source Sans 3",sans-serif;color:var(--ink);background:var(--white);position:relative}
h1,h2,h3,h4{font-family:"Cabin",sans-serif}
a{color:inherit;text-decoration:none}

/* header */
.header{position:absolute;left:0;top:0;width:1200px;height:150px}
.brand{position:absolute;left:0;top:0;width:375px;height:150px}
.brand svg{position:absolute;left:0;top:0}
.brand-name{position:absolute;left:108px;top:18px;width:230px;color:#fff;font-family:"Cabin",sans-serif;font-weight:700;font-size:26px;line-height:27px;text-transform:uppercase}
.brand-mark{position:absolute;left:52px;top:22px;width:44px;height:44px;border:3px solid #fff;border-radius:50%}
.brand-phone{position:absolute;left:50px;top:78px;width:280px;text-align:center;color:#fff;font-family:"Cabin",sans-serif;font-weight:700;font-size:27px}
.brand-phone:before,.brand-phone:after{content:"";position:absolute;top:16px;width:44px;height:2px;background:#fff}
.brand-phone:before{left:2px}.brand-phone:after{right:2px}
.brand-tag{position:absolute;left:52px;top:120px;color:#fff;font-size:10px;font-weight:700;letter-spacing:.2px}
.topbar{position:absolute;left:548px;top:0;width:652px;height:46px;background:var(--navy)}
.topbar svg{position:absolute;left:-14px;top:0}
.topbar .welcome{position:absolute;left:76px;top:12px;color:#fff;font-size:14px}
.topbar .sep{position:absolute;left:325px;top:10px;width:1px;height:26px;background:#fff;opacity:.7}
.topbar .shop{position:absolute;left:342px;top:12px;color:#fff;font-size:14px}
.topbar .soc{position:absolute;top:17px;width:12px;height:12px;border-radius:50%;background:#fff}
.contact-item{position:absolute;top:78px;display:flex;align-items:center;gap:8px;font-size:12.5px;line-height:16px;color:#333}
.contact-item .ring{width:38px;height:38px;border:2px solid var(--red);border-radius:50%;display:flex;align-items:center;justify-content:center;flex:none}

/* nav */
.nav{position:absolute;left:0;top:150px;width:1200px;height:58px;background:var(--navy)}
.nav ul{list-style:none;display:flex;position:absolute;left:90px;top:0;height:58px}
.nav li{color:#fff;font-size:16px;line-height:58px;padding:0 16px;margin-right:13px}
.nav li.active{background:var(--red);position:relative}
.nav li.active:after{content:"";position:absolute;left:50%;bottom:0;margin-left:-6px;border:6px solid transparent;border-bottom-color:#fff}

/* hero */
.hero{position:absolute;left:0;top:208px;width:1200px;height:582px;overflow:hidden}
.hero-photo{position:absolute;inset:0;background:linear-gradient(120deg,#3a3a3a 0%,#9a9a9a 45%,#555 70%,#2a2a2a 100%)}
.hero svg.shape{position:absolute;left:0;top:0}
.ring-icon{position:absolute;border:3px solid var(--red);border-radius:50%}
.ring-icon:after{content:"";position:absolute;left:50%;top:50%;width:10px;height:10px;margin:-5px 0 0 -5px;background:var(--red);border-radius:50%}
.ring-icon.white{border-color:#fff}
.ring-icon.white:after{background:#fff}
.hero h1{position:absolute;left:90px;top:222px;width:400px;color:#fff;font-size:35px;line-height:40px;font-weight:700}
.btn{position:absolute;display:block;background:var(--navy);color:#fff;font-family:"Cabin",sans-serif;font-weight:700;font-size:14px;text-align:center}

/* section headings */
.sec-title{position:absolute;left:0;width:1200px;text-align:center;font-size:33px;font-weight:700;color:var(--navy)}
.sec-title.white{color:#fff}

/* about */
.about h2.lead{position:absolute;left:88px;top:1002px;width:500px;font-size:37px;line-height:40px;color:var(--navy);font-weight:700}
.about p{position:absolute;left:88px;width:480px;font-size:14px;line-height:24.8px;color:#333}
.about .frame{position:absolute;left:690px;top:984px;width:418px;height:426px;border:6px solid var(--red)}
.about .photo{position:absolute;left:650px;top:1021px;width:421px;height:428px;background:linear-gradient(135deg,#1f5fb0 0%,#2e77c9 40%,#6c6258 75%,#3a3a3a 100%)}

/* services */
.services{position:absolute;left:0;top:1505px;width:1200px;height:603px;background:linear-gradient(180deg,#b3252b 0%,#c2282e 50%,#a92128 100%)}
.svc{position:absolute;top:195px;width:243px;height:320px;background:#fff;border-radius:4px;overflow:hidden}
.svc .img{position:absolute;left:0;top:0;width:243px;height:197px}
.svc .ico{position:absolute;left:98px;top:172px;width:48px;height:48px;border-radius:50%;background:var(--navy);border:2px solid #fff;display:flex;align-items:center;justify-content:center}
.svc h3{position:absolute;left:0;top:236px;width:243px;text-align:center;font-size:20px;line-height:22px;color:#222;font-weight:600}
.svc .arr{position:absolute;left:113px;top:290px}

/* products */
.prod{position:absolute;top:2305px;width:316px;height:382px;border:2px solid var(--line);background:#fff}
.prod.on{border:3px solid var(--navy)}
.prod .img{position:absolute;left:70px;top:85px;width:176px;height:200px;border-radius:8px}
.prod-name{position:absolute;top:2700px;font-family:"Cabin",sans-serif;font-weight:700;font-size:21px;color:var(--navy)}
.prod-go{position:absolute;top:2699px;width:30px;height:30px;border:2px solid var(--navy);border-radius:50%;display:flex;align-items:center;justify-content:center}
.dots{position:absolute;left:568px;display:flex;gap:8px}
.dots i{width:10px;height:10px;border-radius:50%;background:#d6d6d6}
.dots i.on{background:var(--navy)}

/* quality band */
.quality{position:absolute;left:0;top:2838px;width:1200px;height:422px;background:linear-gradient(110deg,#1b3165 0%,#2a4a8c 55%,#223d77 100%);overflow:hidden}
.quality .deco{position:absolute;border-radius:50%;background:rgba(255,255,255,.06)}
.quality p{position:absolute;left:230px;top:214px;width:740px;text-align:center;color:#fff;font-size:13.5px;line-height:26px}
.outline-btn{position:absolute;left:498px;top:292px;width:206px;height:40px;border:2px solid #fff;color:#fff;font-family:"Cabin",sans-serif;font-weight:700;font-size:14.5px;line-height:36px;text-align:center}

/* blogs */
.blog-img{position:absolute;top:3460px;width:330px;height:330px}
.blog-card{position:absolute;top:3710px;width:296px;height:245px;background:#fff;box-shadow:0 4px 14px rgba(0,0,0,.18);padding:20px 18px 0}
.blog-card.dark{background:var(--navy);color:#fff}
.blog-card .date{display:flex;align-items:center;gap:7px;font-size:13px;font-weight:700;color:var(--navy)}
.blog-card.dark .date{color:#fff}
.blog-card h4{font-size:16px;line-height:21px;margin-top:12px;font-weight:700}
.blog-card p{font-size:11.5px;line-height:22.5px;margin-top:6px;color:#444}
.blog-card.dark p{color:#e6e9f1}
.blog-card .more{position:absolute;right:30px;bottom:18px;font-size:14px;font-weight:700;color:var(--navy)}
.blog-card.dark .more{color:#fff}

/* footer */
.footer{position:absolute;left:0;top:4083px;width:1200px;height:445px;background:var(--footer);color:#fff}
.footer .stripe{position:absolute;left:0;top:0;height:6px;width:600px;background:var(--red)}
.footer .stripe.b{left:600px;background:var(--navy)}
.footer .halo{position:absolute;left:45px;top:90px;width:280px;height:200px;border-radius:50%;background:rgba(255,255,255,.03)}
.f-brand-mark{position:absolute;left:95px;top:120px;width:48px;height:48px;border:3px solid #fff;border-radius:50%}
.f-brand{position:absolute;left:155px;top:120px;width:210px;font-family:"Cabin",sans-serif;font-weight:700;font-size:25px;line-height:26px;text-transform:uppercase}
.f-phone{position:absolute;left:95px;top:182px;width:255px;text-align:center;font-family:"Cabin",sans-serif;font-weight:700;font-size:26px}
.f-phone:before,.f-phone:after{content:"";position:absolute;top:16px;width:48px;height:2px;background:#fff}
.f-phone:before{left:0}.f-phone:after{right:0}
.f-tag{position:absolute;left:95px;top:222px;font-size:9.5px;font-weight:700}
.f-soc{position:absolute;top:248px;width:34px;height:34px;border:2px solid #fff;border-radius:50%}
.f-col h4{position:absolute;top:84px;font-size:20px;font-weight:600}
.f-col ul{position:absolute;top:130px;list-style:none;font-size:13px;line-height:32px}
.f-contact{position:absolute;left:864px;top:128px;font-size:13px;line-height:24px;width:260px}
.f-contact div{display:flex;gap:10px;margin-bottom:18px}
.f-contact b{font-weight:700}
.f-rule{position:absolute;left:88px;top:385px;width:1024px;height:1px;background:#555}
.f-copy{position:absolute;left:88px;top:402px;font-size:15px;display:flex;align-items:center;gap:6px}
.f-legal{position:absolute;right:88px;top:402px;font-size:15px;display:flex;gap:22px}
</style>
</head>
<body>

<header class="header">
  <div class="brand">
    <svg width="375" height="150" viewBox="0 0 375 150"><polygon points="0,0 375,0 345,150 0,150" fill="#be2228"/><polyline points="371,0 341,150" stroke="#fff" stroke-width="5" fill="none"/></svg>
    <span class="brand-mark"></span>
    <div class="brand-name">Kalena Rebuild Co.</div>
    <div class="brand-phone">555-0142</div>
    <div class="brand-tag">Automotive / Marine / Heavy Duty &nbsp;&nbsp; 2170 Kalena Harbor Rd</div>
  </div>
  <div class="topbar">
    <svg width="20" height="46" viewBox="0 0 20 46"><polygon points="14,0 20,0 20,46 0,46" fill="#213b73"/></svg>
    <span class="welcome">Welcome To Kalena Rebuild Co.</span>
    <span class="sep"></span>
    <span class="shop">Shop Now</span>
    <span class="soc" style="left:450px" aria-label="Social link"></span>
    <span class="soc" style="left:482px" aria-label="Social link"></span>
    <span class="soc" style="left:514px" aria-label="Social link"></span>
    <span class="soc" style="left:546px" aria-label="Social link"></span>
  </div>
  <div class="contact-item" style="left:562px">
    <span class="ring"><svg width="16" height="20" viewBox="0 0 16 20"><path d="M8 0C3.6 0 0 3.5 0 7.8 0 13.6 8 20 8 20s8-6.4 8-12.2C16 3.5 12.4 0 8 0z" fill="#be2228"/><circle cx="8" cy="7.6" r="3" fill="#fff"/></svg></span>
    <span>2170 Kalena Harbor Rd,<br>Lanemoor, OR</span>
  </div>
  <div class="contact-item" style="left:748px">
    <span class="ring"><svg width="18" height="13" viewBox="0 0 18 13"><rect width="18" height="13" rx="2" fill="#be2228"/><path d="M1 1.5l8 6 8-6" stroke="#fff" stroke-width="1.6" fill="none"/></svg></span>
    <span>info@kalenarebuild.com</span>
  </div>
  <div class="contact-item" style="left:980px">
    <span class="ring"><svg width="18" height="18" viewBox="0 0 24 24"><path d="M6.6 10.8a15 15 0 006.6 6.6l2.2-2.2c.3-.3.7-.4 1-.2 1.1.4 2.3.6 3.6.6.6 0 1 .4 1 1V20c0 .6-.4 1-1 1A17 17 0 013 4c0-.6.4-1 1-1h3.5c.6 0 1 .4 1 1 0 1.3.2 2.5.6 3.6.1.3 0 .7-.2 1z" fill="#be2228"/></svg></span>
    <span>808-555-0142</span>
  </div>
</header>

<nav class="nav">
  <ul>
    <li class="active">Home</li><li>Products</li><li>Shop For Batteries</li><li>Auto Repairs</li><li>Battery&nbsp; Brands</li><li>Location</li><li>About Us</li><li>Contact Us</li>
  </ul>
</nav>

<section class="hero">
  <div class="hero-photo" role="img" aria-label="Close-up photo of an engine with pulleys, belts and an alternator"></div>
  <svg class="shape" width="1200" height="582" viewBox="0 0 1200 582">
    <polygon points="0,0 600,0 0,470" fill="#be2228" opacity=".93"/>
    <polygon points="600,0 0,470 0,582 560,582" fill="#a8141b" opacity=".55"/>
    <polygon points="0,470 0,582 470,582" fill="#be2228" opacity=".6"/>
  </svg>
  <span class="ring-icon white" style="left:90px;top:152px;width:60px;height:60px"></span>
  <h1>Your source for New and High-Quality Rebuilt Starters &amp; Alternators.</h1>
  <a class="btn" style="left:90px;top:367px;width:144px;height:40px;line-height:40px">Learn More</a>
</section>

<section class="about">
  <span class="ring-icon" style="left:571px;top:853px;width:58px;height:58px"></span>
  <h2 class="sec-title" style="top:914px">About Kalena Rebuild Co.</h2>
  <h2 class="lead">We sell and rebuild starters &amp; alternators</h2>
  <p style="top:1097px">There are many variations of passages of Lorem Ipsum available, but the majority have suffered alteration in some form, by injected humour, or randomised words which don't look even slightly believable.If you are going to use a passage of Lorem Ipsum, you need to be sure there isn't anything embarrassing hidden in the middle of text. All the Lorem Ipsum generators on the Internet tend to repeat predefined chunks as necessary.</p>
  <p style="top:1271px">But I must explain to you how all this mistaken idea of denouncing pleasure and praising pain was born and I will give you a complete account of the system, and expound the actual teachings of the great explorer of the truth, the master-builder of human happiness.</p>
  <a class="btn" style="left:88px;top:1385px;width:146px;height:40px;line-height:40px">Learn More</a>
  <div class="frame"></div>
  <div class="photo" role="img" aria-label="Photo of a technician testing a vehicle battery with clamps"></div>
</section>

<section class="services">
  <span class="ring-icon white" style="left:571px;top:62px;width:58px;height:58px"></span>
  <h2 class="sec-title white" style="top:124px">Our Services</h2>
  <div class="svc" style="left:88px">
    <div class="img" role="img" aria-label="Photo of a battery being checked under the hood" style="background:linear-gradient(135deg,#d8d8d8,#6f6f6f 60%,#3b3b3b)"></div>
    <span class="ico"><svg width="24" height="18" viewBox="0 0 24 18"><path d="M3 8l2.5-6h13L21 8h1.5v7h-3v2h-2v-2h-11v2h-2v-2h-3V8z" fill="none" stroke="#fff" stroke-width="1.6"/><circle cx="6" cy="11.5" r="1.4" fill="#fff"/><circle cx="18" cy="11.5" r="1.4" fill="#fff"/></svg></span>
    <h3>Orvan Batteries</h3>
    <svg class="arr" width="16" height="12" viewBox="0 0 16 12"><path d="M0 6h13M9 1l5 5-5 5" stroke="#213b73" stroke-width="2" fill="none"/></svg>
  </div>
  <div class="svc" style="left:348px">
    <div class="img" role="img" aria-label="Photo of a high output alternator in an engine bay" style="background:linear-gradient(135deg,#b0221f,#2b5db4 45%,#7d7d7d 80%)"></div>
    <span class="ico"><svg width="24" height="24" viewBox="0 0 24 24"><circle cx="12" cy="12" r="9" fill="none" stroke="#fff" stroke-width="1.6"/><circle cx="12" cy="12" r="3.5" fill="none" stroke="#fff" stroke-width="1.6"/></svg></span>
    <h3>High Output<br>Alternators</h3>
    <svg class="arr" width="16" height="12" viewBox="0 0 16 12"><path d="M0 6h13M9 1l5 5-5 5" stroke="#213b73" stroke-width="2" fill="none"/></svg>
  </div>
  <div class="svc" style="left:608px">
    <div class="img" role="img" aria-label="Photo of interlocking metal gears" style="background:linear-gradient(135deg,#8a8a8a,#2e2e2e 55%,#6a6a6a)"></div>
    <span class="ico"><svg width="22" height="22" viewBox="0 0 22 22"><path d="M3 3l16 16M19 3L3 19" stroke="#fff" stroke-width="2"/></svg></span>
    <h3>Troubleshooting<br>Tips</h3>
    <svg class="arr" width="16" height="12" viewBox="0 0 16 12"><path d="M0 6h13M9 1l5 5-5 5" stroke="#213b73" stroke-width="2" fill="none"/></svg>
  </div>
  <div class="svc" style="left:868px">
    <div class="img" role="img" aria-label="Photo of a mechanic working in a parts shop" style="background:linear-gradient(135deg,#5a5a5a,#b23028 50%,#3c3c3c)"></div>
    <span class="ico"><svg width="22" height="24" viewBox="0 0 22 24"><circle cx="11" cy="7" r="4" fill="none" stroke="#fff" stroke-width="1.6"/><path d="M3 22c0-5 3.5-8 8-8s8 3 8 8z" fill="none" stroke="#fff" stroke-width="1.6"/></svg></span>
    <h3>Current Specials</h3>
    <svg class="arr" width="16" height="12" viewBox="0 0 16 12"><path d="M0 6h13M9 1l5 5-5 5" stroke="#213b73" stroke-width="2" fill="none"/></svg>
  </div>
</section>

<section class="products">
  <span class="ring-icon" style="left:571px;top:2170px;width:58px;height:58px"></span>
  <h2 class="sec-title" style="top:2230px">Our Products</h2>
  <div class="prod on" style="left:88px"><div class="img" role="img" aria-label="Product photo of a battery" style="background:linear-gradient(160deg,#efe7de,#d8a070 55%,#b75a3a)"></div></div>
  <div class="prod" style="left:442px"><div class="img" role="img" aria-label="Product photo of a heavy duty alternator" style="background:radial-gradient(circle,#dcdcdc,#3a3a3a 70%,#fff 72%)"></div></div>
  <div class="prod" style="left:795px"><div class="img" role="img" aria-label="Product photo of an alternator" style="background:radial-gradient(circle,#c8c2b8,#6e6a62 65%,#fff 68%)"></div></div>
  <span class="prod-name" style="left:89px">Product Name</span>
  <span class="prod-go" style="left:372px"><svg width="12" height="10" viewBox="0 0 12 10"><path d="M1 1l4 4-4 4M6 1l4 4-4 4" stroke="#be2228" stroke-width="1.6" fill="none"/></svg></span>
  <span class="prod-name" style="left:441px">Product Name</span>
  <span class="prod-go" style="left:724px"><svg width="12" height="10" viewBox="0 0 12 10"><path d="M1 1l4 4-4 4M6 1l4 4-4 4" stroke="#be2228" stroke-width="1.6" fill="none"/></svg></span>
  <span class="prod-name" style="left:793px">Product Name</span>
  <span class="prod-go" style="left:1076px"><svg width="12" height="10" viewBox="0 0 12 10"><path d="M1 1l4 4-4 4M6 1l4 4-4 4" stroke="#be2228" stroke-width="1.6" fill="none"/></svg></span>
  <div class="dots" style="top:2765px"><i></i><i class="on"></i><i></i><i></i></div>
</section>

<section class="quality">
  <span class="deco" style="left:-110px;top:120px;width:300px;height:300px"></span>
  <span class="deco" style="left:990px;top:20px;width:300px;height:300px"></span>
  <span class="ring-icon white" style="left:571px;top:92px;width:58px;height:58px"></span>
  <h2 class="sec-title white" style="top:156px">We Offer The Best Quality Service</h2>
  <p>There are many variations of passages of Lorem Ipsum available, but the majority have suffered alteration in some form, by injected humour, or randomised words which don't look even slightly believable.</p>
  <a class="outline-btn">Call Us: 808-555-0142</a>
</section>

<section class="blogs">
  <span class="ring-icon" style="left:571px;top:3322px;width:58px;height:58px"></span>
  <h2 class="sec-title" style="top:3385px">Our Latest Blogs</h2>
  <div class="blog-img" style="left:88px;background:linear-gradient(135deg,#2a2a2a,#c0452a 50%,#5a5a5a)" role="img" aria-label="Photo of a red engine block"></div>
  <div class="blog-img" style="left:434px;background:linear-gradient(135deg,#4a4a4a,#9aa0a6 50%,#3a3a3a)" role="img" aria-label="Photo of an engine with an alternator"></div>
  <div class="blog-img" style="left:781px;background:linear-gradient(135deg,#cfd3d6,#7a7f85 50%,#3e4a5e)" role="img" aria-label="Photo of a mechanic working beside a car"></div>

  <article class="blog-card" style="left:105px">
    <div class="date"><svg width="14" height="14" viewBox="0 0 14 14"><circle cx="7" cy="7" r="6" fill="none" stroke="currentColor" stroke-width="1.4"/><path d="M7 3.5V7l2.5 1.5" stroke="currentColor" stroke-width="1.4" fill="none"/></svg>09-06-2019</div>
    <h4>Sed ut perspiciatis unde omnis iste natus error sit</h4>
    <p>It is a long established fact that a reader will be distracted by the readable content of a page when looking at its layout. The point of using Lorem Ipsum is that it has a more.</p>
    <span class="more">Read More &raquo;</span>
  </article>
  <article class="blog-card dark" style="left:452px">
    <div class="date"><svg width="14" height="14" viewBox="0 0 14 14"><circle cx="7" cy="7" r="6" fill="none" stroke="currentColor" stroke-width="1.4"/><path d="M7 3.5V7l2.5 1.5" stroke="currentColor" stroke-width="1.4" fill="none"/></svg>09-06-2019</div>
    <h4>Sed ut perspiciatis unde omnis iste natus error sit</h4>
    <p>It is a long established fact that a reader will be distracted by the readable content of a page when looking at its layout. The point of using Lorem Ipsum is that it has a more.</p>
    <span class="more">Read More &raquo;</span>
  </article>
  <article class="blog-card" style="left:798px">
    <div class="date"><svg width="14" height="14" viewBox="0 0 14 14"><circle cx="7" cy="7" r="6" fill="none" stroke="currentColor" stroke-width="1.4"/><path d="M7 3.5V7l2.5 1.5" stroke="currentColor" stroke-width="1.4" fill="none"/></svg>09-06-2019</div>
    <h4>Sed ut perspiciatis unde omnis iste natus error sit</h4>
    <p>It is a long established fact that a reader will be distracted by the readable content of a page when looking at its layout. The point of using Lorem Ipsum is that it has a more.</p>
    <span class="more">Read More &raquo;</span>
  </article>
  <div class="dots" style="top:4003px"><i></i><i class="on"></i><i></i><i></i></div>
</section>

<footer class="footer">
  <span class="stripe"></span><span class="stripe b"></span>
  <span class="halo"></span>
  <span class="f-brand-mark"></span>
  <div class="f-brand">Kalena Rebuild Co.</div>
  <div class="f-phone">555-0142</div>
  <div class="f-tag">Automotive / Marine / Heavy Duty &nbsp;&nbsp; 2170 Kalena Harbor Rd</div>
  <span class="f-soc" style="left:122px" aria-label="Social link"></span>
  <span class="f-soc" style="left:176px" aria-label="Social link"></span>
  <span class="f-soc" style="left:230px" aria-label="Social link"></span>
  <span class="f-soc" style="left:284px" aria-label="Social link"></span>

  <div class="f-col"><h4 style="left:450px">Quick Links</h4>
    <ul style="left:450px"><li>Home</li><li>About Us</li><li>Our Products</li><li>Services</li><li>Blogs</li><li>Contact Us</li></ul></div>
  <div class="f-col"><h4 style="left:648px">Services</h4>
    <ul style="left:648px"><li>Orvan Batteries</li><li>High Output Alternators</li><li>Troubleshooting</li><li>Current Specials</li></ul></div>
  <div class="f-col"><h4 style="left:864px">Contact Us</h4></div>
  <div class="f-contact">
    <div><svg width="14" height="18" viewBox="0 0 16 20" style="flex:none;margin-top:3px"><path d="M8 0C3.6 0 0 3.5 0 7.8 0 13.6 8 20 8 20s8-6.4 8-12.2C16 3.5 12.4 0 8 0z" fill="#fff"/><circle cx="8" cy="7.6" r="3" fill="#2b2b2b"/></svg><span><b>Location:</b> 2170 Kalena Harbor Rd,<br>Lanemoor, OR 97999.</span></div>
    <div><svg width="16" height="16" viewBox="0 0 24 24" style="flex:none;margin-top:4px"><path d="M6.6 10.8a15 15 0 006.6 6.6l2.2-2.2c.3-.3.7-.4 1-.2 1.1.4 2.3.6 3.6.6.6 0 1 .4 1 1V20c0 .6-.4 1-1 1A17 17 0 013 4c0-.6.4-1 1-1h3.5c.6 0 1 .4 1 1 0 1.3.2 2.5.6 3.6.1.3 0 .7-.2 1z" fill="#fff"/></svg><span><b>Phone:</b> 808-555-0142</span></div>
    <div><svg width="16" height="12" viewBox="0 0 18 13" style="flex:none;margin-top:6px"><rect width="18" height="13" rx="2" fill="#fff"/><path d="M1 1.5l8 6 8-6" stroke="#2b2b2b" stroke-width="1.6" fill="none"/></svg><span><b>Email:</b> info@kalenarebuild.com</span></div>
  </div>
  <span class="f-rule"></span>
  <div class="f-copy"><svg width="16" height="16" viewBox="0 0 16 16"><circle cx="8" cy="8" r="7" fill="none" stroke="#fff" stroke-width="1.3"/><path d="M10.5 6a3 3 0 100 4" stroke="#fff" stroke-width="1.3" fill="none"/></svg>Copyright. All Rights Reserved</div>
  <div class="f-legal"><span>Terms &amp; Conditions</span><span>Privacy Policy</span></div>
</footer>

</body>
</html>
```